Wedding Music Playlist Template

Hi, I'm a wedding musician and I'd like a 1 pager wedding music template created. It needs to be editable for future weddings.

At the top of the template:
Bride First Name & Groom First Name plus 's WEDDING
Date of Wedding:
Venue name:

(The form needs to be flexible where I can remove/interchange Prelude Ceremony / Ceremony / Canapes / Reception) as sometimes I will play music just for a Ceremony sometimes for both Ceremony/Canapes or sometimes just the reception only or all of the above.

Section 1: Prelude Ceremony (this could be up to 5 songs)

Section 2: Ceremony
Processional (this is sometimes 1 or 2 songs)
Signing of Papers (this is sometimes 1 or 2 songs)
Recessional (1 song)

Section 3: Canapes

Section 4: Reception

Within each section
Artist
Song

I'd also like the template to feature
logo (attached) and social media links
website URL tolvercade.com.au
instagram: tolvercademusic
facebook: tolvercadepianist
soundcloud: keyglow_nuptials

I see the form/template serving two purposes.
1) I'll send back to the bride when she books me for a wedding and she may socialise it.
2) Posting on instagram as I perform at each wedding and attract engaged brides looking for wedding pianist or even just ideas for wedding music.
Updates

Target Market(s)

Engaged Couples looking for wedding music or suggested music for wedding

Industry/Entity Type

Wedding

Requirements
Must have
• Please see project description.
Nice to have
• Background wedding image with text overlayed

```html
<!DOCTYPE html>
<html lang="en">
<head>
<meta charset="utf-8">
<title>Wedding Music Playlist</title>
<link href="https://fonts.googleapis.com/css2?family=Great+Vibes&family=Cormorant+Garamond:wght@500;600&family=Montserrat:wght@500;700&display=swap" rel="stylesheet">
<style>
  :root {
    --backdrop: #e9e9e9;
    --paper: #ffffff;
    --teal: #1fa3a6;
    --ink: #3a3a3a;
    --muted: #8a8a8a;
    --photo-light: #f3eeec;
    --photo-mid: #e3d3cc;
    --photo-rose: #c9867c;
  }
  * { margin: 0; padding: 0; box-sizing: border-box; }
  html, body { width: 1200px; height: 686px; overflow: hidden; background: var(--backdrop); }
  .flyer {
    position: absolute; left: 366px; top: 13px;
    width: 467px; height: 660px;
    background: var(--paper);
    box-shadow: 0 2px 10px rgba(0,0,0,.15);
    font-family: "Cormorant Garamond", serif;
    color: var(--ink);
    text-align: center;
  }
  .hero { position: absolute; left: 0; top: 0; width: 467px; height: 230px; }
  .brand {
    position: absolute; left: 22px; top: 22px;
    display: flex; align-items: center; gap: 6px; text-align: left;
  }
  .brand-dot { width: 24px; height: 24px; border-radius: 50%; background: #1d1d1d; }
  .brand-name { font-family: "Montserrat", sans-serif; font-weight: 700; font-size: 9px; letter-spacing: .5px; color: #1d1d1d; }
  .brand-tag { font-family: "Montserrat", sans-serif; font-weight: 500; font-size: 5px; color: #555; }
  .couple {
    position: absolute; left: 0; right: 0; top: 222px;
    font-family: "Great Vibes", cursive; font-size: 46px; color: var(--teal); line-height: 1;
  }
  .date { position: absolute; left: 0; right: 0; top: 270px; font-size: 11px; font-weight: 600; }
  .date-script { font-family: "Great Vibes", cursive; color: var(--teal); font-size: 22px; margin-left: 10px; }
  .venue { position: absolute; left: 0; right: 0; top: 292px; font-size: 10px; font-weight: 600; letter-spacing: .6px; }
  .program { position: absolute; left: 0; right: 0; top: 308px; }
  .section-title { font-size: 7px; font-weight: 600; letter-spacing: .6px; color: var(--muted); margin-top: 6px; }
  .sub { font-size: 6.5px; font-weight: 600; color: var(--ink); margin-top: 3px; }
  .song { font-size: 6px; font-style: italic; color: var(--muted); line-height: 11px; }
  .contacts {
    position: absolute; left: 30px; right: 30px; top: 600px;
    display: flex; flex-wrap: wrap; justify-content: center; gap: 8px 34px;
    font-family: "Montserrat", sans-serif; font-size: 6px; color: #555;
  }
  .contact { display: flex; align-items: center; gap: 5px; }
  .contact-mark { width: 9px; height: 9px; border-radius: 50%; background: var(--teal); }
</style>
</head>
<body>
  <main class="flyer">
    <svg class="hero" viewBox="0 0 467 230" role="img" aria-label="Photograph of a bride's hands holding a bouquet of red and white roses">
      <defs>
        <linearGradient id="heroTone" x1="0" y1="0" x2="1" y2="1">
          <stop offset="0" stop-color="var(--photo-light)"/>
          <stop offset=".55" stop-color="var(--photo-mid)"/>
          <stop offset="1" stop-color="var(--photo-rose)"/>
        </linearGradient>
      </defs>
      <path d="M0 0 H467 V195 C400 175 330 195 250 190 C170 185 80 160 0 165 Z" fill="url(#heroTone)"/>
    </svg>

    <div class="brand">
      <span class="brand-dot"></span>
      <div>
        <div class="brand-name">TOLVERCADE</div>
        <div class="brand-tag">Wedding &amp; Event Pianist</div>
      </div>
    </div>

    <h1 class="couple">Rosalind &amp; Jonah's</h1>
    <p class="date">SAT August 26<sup>th</sup> 2017 <span class="date-script">Wedding</span></p>
    <p class="venue">ELMSWORTH HALL</p>

    <section class="program">
      <h2 class="section-title">SECTION 1: PRELUDE CEREMONY</h2>
      <p class="song">Artist (Song)</p>
      <p class="song">Morning Light</p>
      <p class="song">Quiet River</p>
      <p class="song">Still Waters</p>
      <p class="song">Golden Hour</p>

      <h2 class="section-title">SECTION 2: CEREMONY</h2>
      <p class="sub">Processional</p>
      <p class="song">First Light</p>
      <p class="sub">Signing of Papers</p>
      <p class="song">Artist (Song)</p>
      <p class="sub">Recessional</p>
      <p class="song">Open Road</p>

      <h2 class="section-title">SECTION 3: CANAPES</h2>
      <h2 class="section-title">SECTION 4: RECEPTION</h2>
    </section>

    <footer class="contacts">
      <span class="contact"><span class="contact-mark"></span>http://tolvercade.com.au/</span>
      <span class="contact"><span class="contact-mark"></span>tolvercademusic</span>
      <span class="contact"><span class="contact-mark"></span>tolvercadepianist</span>
      <span class="contact"><span class="contact-mark"></span>keyglow_nuptials</span>
    </footer>
  </main>
</body>
</html>
```